Orbell Consulting- executive coaching business

looking for business card design for a newly started coaching business.
specialising in Exective coaching, Leadership, NLP and Motivation.
Looking for a simple, classy design using the existing logo attached and colour themes that complement the logo.
No red or orange in the business card design please.

Target Market(s)

Defence and Veteran community

Industry/Entity Type

Life Coaching

Contact Information for Business Card

looking for business cards for newly started coaching business.
specialising in Exective Coaching, Leadership, NLP and Motivation

Font styles to use
Serif
Script

Colors
0556a4
3176b5
86cfc6
33b8a4

Requirements
Must have
• Logo
• Email address- Jess@orbellconsulting.com.au
• Contact number
• Services provided - Executive Coaching, Leadership, NLP and Motivational Mapping.
Nice to have
• Same colours as logo
Should not have
• Red or orange

```html
<!DOCTYPE html>
<html lang="en">
<head>
<meta charset="utf-8">
<title>Orbell Consulting – Business Card</title>
<link rel="stylesheet" href="https://fonts.googleapis.com/css2?family=Open+Sans:wght@400;600&display=swap">
<style>
  :root {
    --page-bg: #ecebe8;
    --card-white: #ffffff;
    --brand-blue: #1b75bc;
    --brand-green: #2db573;
    --text-grey: #5f6368;
    --ink-white: #ffffff;
  }
  * { box-sizing: border-box; margin: 0; padding: 0; }
  html, body {
    width: 1200px; height: 1200px; overflow: hidden;
    background: var(--page-bg);
    font-family: "Open Sans", Arial, sans-serif;
  }
  .canvas {
    width: 1200px; height: 1200px;
    display: flex; flex-direction: column; align-items: center; justify-content: center;
    gap: 60px;
  }
  .card {
    position: relative;
    width: 840px; height: 480px;
    overflow: hidden;
    box-shadow: 0 6px 18px rgba(0,0,0,0.18);
  }

  /* Front */
  .card--front { background: var(--card-white); }
  .brand {
    position: absolute; right: 60px; top: 50px;
    display: flex; flex-direction: column; align-items: flex-end; gap: 14px;
  }
  .brand__dot {
    width: 78px; height: 78px; border-radius: 50%;
    border: 4px solid var(--brand-blue);
    margin-right: 150px;
  }
  .brand__name {
    color: var(--brand-blue); font-weight: 600; font-size: 36px;
    letter-spacing: 0.5px; text-transform: uppercase; line-height: 1;
  }
  .person { position: absolute; left: 50px; top: 206px; }
  .person__name { color: var(--brand-blue); font-size: 34px; font-weight: 400; line-height: 1.1; }
  .person__title { color: var(--text-grey); font-size: 21px; margin-top: 14px; }
  .divider {
    position: absolute; left: 50px; right: 50px; top: 258px;
    height: 2px; background: var(--brand-green);
  }
  .services {
    position: absolute; right: 50px; top: 272px;
    list-style: none; text-align: right;
  }
  .services li {
    color: var(--brand-blue); font-size: 21px; line-height: 34px;
    display: flex; align-items: center; justify-content: flex-end; gap: 12px;
  }
  .services li::after {
    content: ""; width: 9px; height: 9px; border-radius: 50%;
    background: var(--brand-green);
  }
  .contact { position: absolute; left: 50px; top: 330px; list-style: none; }
  .contact li {
    display: flex; align-items: center; gap: 14px;
    color: var(--text-grey); font-size: 21px; line-height: 36px;
  }
  .contact svg { width: 20px; height: 20px; fill: var(--brand-green); }
  .band-green {
    position: absolute; left: 0; right: 0; bottom: 0;
    height: 18px; background: var(--brand-green);
  }
  .web-tab {
    position: absolute; right: 0; bottom: 18px;
    width: 330px; height: 44px;
    background: var(--brand-blue);
    clip-path: polygon(18px 0, 100% 0, 100% 100%, 0 100%);
    color: var(--ink-white); font-size: 19px;
    display: flex; align-items: center; padding-left: 40px;
  }

  /* Back */
  .card--back {
    background: var(--brand-blue);
    display: flex; flex-direction: column; align-items: center; justify-content: center; gap: 26px;
  }
  .card--back .brand__dot {
    width: 140px; height: 140px; border-color: var(--ink-white); border-width: 6px; margin: 0;
  }
  .card--back .brand__name { color: var(--ink-white); font-size: 54px; }
</style>
</head>
<body>
<main class="canvas">

  <section class="card card--front" aria-label="Business card front">
    <div class="brand">
      <span class="brand__dot"></span>
      <span class="brand__name">Orbell Consulting</span>
    </div>

    <div class="person">
      <p class="person__name">Jess Harlow</p>
      <p class="person__title">Managing Partner</p>
    </div>

    <div class="divider"></div>

    <ul class="services">
      <li>Executive Coaching</li>
      <li>Leadership</li>
      <li>NLP and Motivational Mapping</li>
    </ul>

    <ul class="contact">
      <li>
        <svg viewBox="0 0 24 24" aria-hidden="true"><path d="M6.6 10.8a15.1 15.1 0 0 0 6.6 6.6l2.2-2.2a1 1 0 0 1 1-.25 11.4 11.4 0 0 0 3.6.57 1 1 0 0 1 1 1V20a1 1 0 0 1-1 1A17 17 0 0 1 3 4a1 1 0 0 1 1-1h3.5a1 1 0 0 1 1 1c0 1.25.2 2.45.57 3.57a1 1 0 0 1-.25 1z"/></svg>
        000.000.0000
      </li>
      <li>
        <svg viewBox="0 0 24 24" aria-hidden="true"><path d="M2 5h20v14H2z M3.5 6.5 12 13l8.5-6.5v-.5h-17z" fill-rule="evenodd"/><path d="M3 6l9 7 9-7" fill="none" stroke="#fff" stroke-width="1.6"/></svg>
        Jess@orbellconsulting.com.au
      </li>
    </ul>

    <div class="band-green"></div>
    <div class="web-tab">www.orbellconsulting.com.au</div>
  </section>

  <section class="card card--back" aria-label="Business card back">
    <span class="brand__dot"></span>
    <span class="brand__name">Orbell Consulting</span>
  </section>

</main>
</body>
</html>
```